Park Company Mobile Application Design

We are looking for deisgn of the mobile application for the parking company. More details about the parking company you can find on the following web site: www.tvr.mk.
As well we attached the parking card that this company is issuing. As you may see their preferred color is green.
Attached you can find screens that we are planning to implement in the mobile application.
If you need more details please contact us on goran@brelo.mk.

Thanks,
Goran Dimovski
Brelo Group

```html
<!DOCTYPE html>
<html lang="en">
<head>
<meta charset="utf-8">
<title>Parking App – Start Parking</title>
<link href="https://fonts.googleapis.com/css2?family=Poppins:wght@400;500;600;700&display=swap" rel="stylesheet">
<style>
  :root{
    --green-dark:#0b4a1a;
    --green-mid:#1f7a2c;
    --green-light:#4db848;
    --field-border:#d4d4d4;
    --text-main:#2b2b2b;
    --text-muted:#6f6f6f;
    --status-pill:#555555;
    --panel-top:#d9d9d9;
    --panel-bottom:#ffffff;
    --white:#ffffff;
    --bg-photo-a:#eef1f3;
    --bg-photo-b:#dfe4e6;
  }
  *{box-sizing:border-box;margin:0;padding:0}
  html,body{width:1200px;height:2595px;overflow:hidden}
  body{font-family:"Poppins",sans-serif;background:var(--white);position:relative;color:var(--text-main)}
  .backdrop{position:absolute;inset:0;background:linear-gradient(180deg,var(--bg-photo-a) 0%,var(--bg-photo-b) 55%,var(--bg-photo-a) 100%)}
  .status-bar .time{position:absolute;left:64px;top:26px;width:160px;height:70px;border-radius:35px;background:var(--status-pill);color:var(--white);font-size:42px;font-weight:600;display:flex;align-items:center;justify-content:center}
  .status-bar .indicators{position:absolute;left:1010px;top:44px;display:flex;align-items:center;gap:16px;font-size:38px;font-weight:500;color:var(--text-main)}
  .menu-button{position:absolute;left:106px;top:182px;width:80px;height:74px;display:flex;flex-direction:column;justify-content:space-between}
  .menu-button span{display:block;height:17px;background:var(--green-dark);border-radius:2px}
  .brand{position:absolute;left:400px;top:200px;width:480px;text-align:center;display:flex;align-items:center;justify-content:center;gap:20px}
  .brand .dot{width:44px;height:44px;border-radius:50%;background:var(--green-dark)}
  .brand .name{font-size:54px;font-weight:700;color:var(--green-dark);line-height:1.1}
  .user-name{position:absolute;left:960px;top:200px;font-size:40px;font-weight:600;color:var(--text-muted)}
  .pin{position:absolute;left:320px;top:555px;width:576px;height:710px}
  .field{position:absolute;left:182px;width:838px;height:122px;background:var(--white);border:3px solid var(--field-border);border-radius:20px;display:flex;align-items:center;padding-left:40px;gap:28px;font-size:40px}
  .field svg{width:44px;height:44px;fill:var(--green-dark)}
  .field.location{top:1462px}
  .field.duration{top:1622px}
  .field.plate{top:1782px}
  .primary-button{position:absolute;left:182px;top:1971px;width:838px;height:122px;border-radius:26px;background:var(--green-dark);color:var(--white);font-size:40px;font-weight:600;display:flex;align-items:center;justify-content:center;border:none}
  .tab-bar{position:absolute;left:0;top:2256px;width:1200px;height:339px;border-radius:48px 48px 0 0;background:linear-gradient(180deg,var(--panel-top) 0%,var(--panel-bottom) 75%)}
  .tab{position:absolute;top:2165px;width:280px;display:flex;flex-direction:column;align-items:center}
  .tab svg{width:200px;height:175px}
  .tab .label{margin-top:18px;font-size:40px;color:var(--text-main)}
  .tab.active .label{color:var(--green-dark)}
  .tab.parking{left:94px}
  .tab.card{left:458px}
  .tab.report{left:826px}
</style>
</head>
<body>
  <div class="backdrop" role="img" aria-label="Faded photograph of an office building facade"></div>

  <header class="status-bar">
    <div class="time">2:00</div>
    <div class="indicators">
      <svg width="52" height="36" viewBox="0 0 52 36"><rect x="0" y="26" width="8" height="10" fill="#2b2b2b"/><rect x="13" y="18" width="8" height="18" fill="#2b2b2b"/><rect x="26" y="9" width="8" height="27" fill="#2b2b2b"/><rect x="39" y="0" width="8" height="36" fill="#2b2b2b"/></svg>
      <span>4G</span>
      <svg width="66" height="36" viewBox="0 0 66 36"><rect x="2" y="2" width="56" height="32" rx="7" fill="none" stroke="#2b2b2b" stroke-width="4"/><rect x="8" y="8" width="36" height="20" rx="3" fill="#2b2b2b"/><rect x="60" y="12" width="5" height="12" rx="2" fill="#2b2b2b"/></svg>
    </div>
  </header>

  <div class="menu-button"><span></span><span></span><span></span></div>

  <div class="brand"><span class="dot"></span><span class="name">ГРАДСКИ<br>ПАРКИНГ</span></div>

  <div class="user-name">VERA</div>

  <svg class="pin" viewBox="0 0 180 222">
    <defs>
      <linearGradient id="pinGradient" x1="0" x2="1" y1="0" y2="0">
        <stop offset="0" stop-color="#4db848"/>
        <stop offset="1" stop-color="#0a4512"/>
      </linearGradient>
    </defs>
    <path d="M90 8C45 8 10 43 10 88c0 52 80 126 80 126s80-74 80-126C170 43 135 8 90 8z" fill="url(#pinGradient)" stroke="#ffffff" stroke-width="12" stroke-linejoin="round"/>
    <circle cx="90" cy="84" r="30" fill="none" stroke="#ffffff" stroke-width="14"/>
  </svg>

  <div class="field location">
    <svg viewBox="0 0 24 24"><path d="M12 2C8 2 5 5 5 9c0 5 7 13 7 13s7-8 7-13c0-4-3-7-7-7zm0 10a3 3 0 1 1 0-6 3 3 0 0 1 0 6z"/></svg>
    <span>ABC Stree City 12345</span>
  </div>
  <div class="field duration">
    <svg viewBox="0 0 24 24"><path d="M12 2a10 10 0 1 0 0 20 10 10 0 0 0 0-20zm1 10.4 3.5 2.1-1 1.6L11 13V6h2z"/></svg>
    <span>15 min</span>
  </div>
  <div class="field plate">
    <svg viewBox="0 0 24 24"><path d="M5 11l1.6-4.5C6.9 5.6 7.7 5 8.6 5h6.8c.9 0 1.7.6 2 1.5L19 11c1.1.2 2 1.1 2 2.3V18h-2v2h-3v-2H8v2H5v-2H3v-4.7C3 12.1 3.9 11.2 5 11zm2.2 0h9.6l-1.1-3.3c-.1-.4-.5-.7-.9-.7H9.2c-.4 0-.8.3-.9.7zM6.5 16a1.5 1.5 0 1 0 0-3 1.5 1.5 0 0 0 0 3zm11 0a1.5 1.5 0 1 0 0-3 1.5 1.5 0 0 0 0 3z"/></svg>
    <span>SK5555SS</span>
  </div>

  <button class="primary-button">Button 3</button>

  <nav class="tab-bar"></nav>

  <div class="tab parking active">
    <svg viewBox="0 0 100 88">
      <rect x="6" y="6" width="88" height="78" rx="14" fill="#ffffff"/>
      <path d="M34 26a22 22 0 0 1 32 0M40 32a13 13 0 0 1 20 0" fill="none" stroke="#1f7a2c" stroke-width="5" stroke-linecap="round"/>
      <circle cx="50" cy="38" r="4" fill="#1f7a2c"/>
      <path d="M20 58l6-12c1-3 4-4 7-4h34c3 0 6 1 7 4l6 12v20h-9v-6H29v6h-9z" fill="#1f7a2c"/>
      <circle cx="31" cy="62" r="4" fill="#ffffff"/><circle cx="69" cy="62" r="4" fill="#ffffff"/>
    </svg>
    <span class="label">Lorem</span>
  </div>

  <div class="tab card">
    <svg viewBox="0 0 100 88">
      <rect x="8" y="14" width="84" height="62" rx="10" fill="#ffffff" stroke="#555555" stroke-width="4"/>
      <rect x="14" y="20" width="72" height="50" rx="6" fill="#555555"/>
      <rect x="20" y="28" width="26" height="34" rx="3" fill="#ffffff"/>
      <circle cx="33" cy="40" r="6" fill="#555555"/>
      <path d="M24 60c2-7 6-9 9-9s7 2 9 9z" fill="#555555"/>
      <rect x="52" y="32" width="28" height="5" fill="#ffffff"/><rect x="52" y="43" width="28" height="5" fill="#ffffff"/><rect x="52" y="54" width="20" height="5" fill="#ffffff"/>
    </svg>
    <span class="label">Lorem</span>
  </div>

  <div class="tab report">
    <svg viewBox="0 0 100 88">
      <path d="M50 6L94 82H6z" fill="#555555" stroke="#ffffff" stroke-width="5" stroke-linejoin="round"/>
      <rect x="46" y="32" width="8" height="28" rx="3" fill="#ffffff"/>
      <circle cx="50" cy="70" r="5" fill="#ffffff"/>
    </svg>
    <span class="label">Lorem</span>
  </div>
</body>
</html>
```